Business Card, A4 Letter Head and DL Envelope for Vantrelle

We are looking for a design for our Business Card, A4 Letter Head and DL Envelope.

Vantrelle is a distributor of promotional products. We specialize in a range of branded promotional products, these include pens, polo shirts, key rings, drink bottles, uniforms and bags to name a few. We are experts in marketing and assist companies in choosing the right promotional product for their needs. We will predominately be an online business where customers visit our website and browse our range of promotional products and branding options.

Our colours are black, red, white and grey.

Files must be supplied in eps, pdf and ai format.

Please display the following information:
Corbin Hale
Account Manager
Suite xxx, 214 Dawlish Parade Melbourne, Victoria 3000
Phone +61 3 5550 1827
Mobile +61 455 501 936
sales@vantrelle.com.au
www.vantrelle.com.au

```html
<!DOCTYPE html>
<html lang="en">
<head>
<meta charset="utf-8">
<title>Vantrelle Stationery</title>
<link rel="stylesheet" href="https://fonts.googleapis.com/css2?family=Questrial&display=swap">
<style>
:root{
  --backdrop:#6e6e6e;
  --paper:#ffffff;
  --brand-red:#c11d24;
  --ink:#4a4a4a;
  --ink-dark:#2b2b2b;
  --shadow:rgba(0,0,0,0.35);
}
*{margin:0;padding:0;box-sizing:border-box}
html,body{width:1200px;height:1000px;overflow:hidden}
body{background:var(--backdrop);font-family:"Questrial",sans-serif;color:var(--ink);position:relative}
.sheet{position:absolute;background:var(--paper);box-shadow:2px 3px 6px var(--shadow);overflow:hidden}
.band{position:absolute;left:0;right:0;background:var(--brand-red)}
.brand{position:absolute;display:flex;align-items:center;gap:8px;color:var(--ink);letter-spacing:0.5px;white-space:nowrap}
.brand-dot{border-radius:50%;background:var(--brand-red);flex:none}

/* Letterhead */
.letterhead{left:46px;top:24px;width:529px;height:683px}
.letterhead .band-top{top:0;height:33px}
.letterhead .brand{left:32px;top:50px;font-size:17px}
.letterhead .brand-dot{width:30px;height:30px}
.letterhead .rule{position:absolute;left:0;right:0;top:647px;height:2px;background:var(--brand-red)}
.letterhead .footer{position:absolute;left:0;right:0;top:654px;text-align:center;font-size:7px;line-height:11px;color:var(--ink-dark)}
.sep{color:var(--brand-red);padding:0 3px}

/* Business card front */
.card-front{left:619px;top:86px;width:436px;height:260px}
.card-front .band-top{top:0;height:189px}
.card-front .person{position:absolute;right:28px;top:14px;text-align:left;color:var(--paper)}
.card-front .person-name{font-size:23px;letter-spacing:0.6px;font-weight:400}
.card-front .person-role{font-size:14px;margin-top:1px}
.contacts{position:absolute;left:34px;top:98px;color:var(--paper);font-size:13px;line-height:16px;list-style:none}
.contacts li{display:flex;align-items:center;gap:6px}
.icon{width:12px;height:12px;border-radius:50%;background:var(--paper);color:var(--brand-red);font-size:8px;display:inline-flex;align-items:center;justify-content:center;line-height:1}
.card-front .address{position:absolute;left:34px;top:149px;color:var(--paper);font-size:13px;line-height:15px;font-style:normal}
.card-front .brand{left:120px;top:205px;font-size:18px}
.card-front .brand-dot{width:34px;height:34px}

/* Business card back */
.card-back{left:712px;top:400px;width:435px;height:259px}
.card-back .brand{left:0;right:0;top:40px;flex-direction:column;gap:12px;font-size:23px}
.card-back .brand-dot{width:68px;height:68px}
.card-back .band-web{top:167px;height:22px;display:flex;align-items:center;justify-content:center;gap:6px;color:var(--paper);font-size:13px}

/* Envelope */
.envelope{left:249px;top:724px;width:587px;height:256px}
.envelope .band-top{top:0;height:33px}
.envelope .brand{left:36px;top:60px;font-size:12px;gap:6px}
.envelope .brand-dot{width:22px;height:22px}
.envelope .return{position:absolute;left:36px;top:92px;border-left:1px solid var(--brand-red);padding-left:4px;font-size:6.5px;line-height:9px;color:var(--brand-red)}
.envelope .return .tel{color:var(--ink-dark);display:flex;align-items:center;gap:3px}
.envelope .return .icon{width:7px;height:7px;background:var(--brand-red);color:var(--paper);font-size:5px}
.envelope .band-bottom{top:239px;height:9px}
</style>
</head>
<body>

<section class="sheet letterhead" aria-label="A4 letterhead">
  <div class="band band-top"></div>
  <div class="brand"><span class="brand-dot"></span>VANTRELLE</div>
  <div class="rule"></div>
  <div class="footer">
    <p>www.vantrelle.com.au<span class="sep">|</span>Suite xxx, 214 Dawlish Parade, Melbourne, Victoria 3000</p>
    <p>Tel: +61 3 5550 1827<span class="sep">|</span>Mob: +61 455 501 936<span class="sep">|</span>e-mail : sales@vantrelle.com.au</p>
  </div>
</section>

<section class="sheet card-front" aria-label="Business card front">
  <div class="band band-top"></div>
  <div class="person">
    <h1 class="person-name">Corbin Hale</h1>
    <p class="person-role">Account Manager</p>
  </div>
  <ul class="contacts">
    <li><span class="icon">M</span>+61 455 501 936</li>
    <li><span class="icon">T</span>+61 3 5550 1827</li>
    <li><span class="icon">e</span>sales@vantrelle.com.au</li>
  </ul>
  <address class="address">Suite xxx, 214 Dawlish Parade<br>Melbourne, Victoria 3000</address>
  <div class="brand"><span class="brand-dot"></span>VANTRELLE</div>
</section>

<section class="sheet card-back" aria-label="Business card back">
  <div class="brand"><span class="brand-dot"></span>VANTRELLE</div>
  <div class="band band-web"><span class="icon">w</span>www.vantrelle.com.au</div>
</section>

<section class="sheet envelope" aria-label="DL envelope">
  <div class="band band-top"></div>
  <div class="brand"><span class="brand-dot"></span>VANTRELLE</div>
  <div class="return">
    <p class="tel"><span class="icon">T</span>+61 3 5550 1827</p>
    <p>Suite xxx, 214 Dawlish Parade</p>
    <p>Melbourne, Victoria 3000</p>
  </div>
  <div class="band band-bottom"></div>
</section>

</body>
</html>
```